Australian Civil Construction, Quarry & Mining Services needs a business card

We need a business card designed for our Civil Construction, Quarry & Mining Services based in the country in Australia.
Our Company Brackley Earthworks provide innovate solutions for infrastructure, agricultural and mining (aggregate, sand, roadbase) industry.
We would like our business cards to be double sided
Front of card: black background or something that resembles our business colours. (it doesn't have to be black we are open to options)
- Company name - Brackley Earthworks
- Either our logo or some sort of icon/picture that resembles our business
- Website - https://brackleyearthworks.com.au/
- We will have a number of different names, positions descriptions, phone numbers and emails on separate cards for each of our managers/directors

```html
<!DOCTYPE html>
<html lang="en">
<head>
<meta charset="UTF-8">
<title>Brackley Earthworks – Business Card</title>
<link rel="stylesheet" href="https://fonts.googleapis.com/css2?family=Montserrat:wght@400;500;700;800&display=swap">
<style>
  :root {
    --bg: #d9dbde;
    --card-black: #1b1718;
    --card-white: #ffffff;
    --orange: #f0871c;
    --shadow-grey: #cfcfcf;
    --text-light: #ffffff;
    --text-soft: #e6e6e6;
  }
  * { box-sizing: border-box; margin: 0; padding: 0; }
  html, body {
    width: 1200px; height: 900px; overflow: hidden;
    background: var(--bg);
    font-family: "Montserrat", sans-serif;
  }
  .canvas { position: relative; width: 1200px; height: 900px; }

  .card {
    position: absolute;
    left: 250px;
    width: 700px; height: 400px;
    border-radius: 22px;
    background: var(--card-black);
    overflow: hidden;
    box-shadow: 0 10px 30px rgba(0,0,0,.25);
  }
  .card--front { top: 30px; }
  .card--back  { top: 470px; }

  /* Front */
  .front-badge {
    position: absolute; left: 258px; top: 70px;
    width: 184px; height: 184px; border-radius: 50%;
    background: var(--card-white);
    box-shadow: 6px 4px 0 var(--shadow-grey);
    display: flex; align-items: center; justify-content: center;
    text-align: center;
  }
  .badge-name {
    font-weight: 800; font-size: 19px; line-height: 1.15;
    color: var(--orange); text-transform: uppercase; letter-spacing: .5px;
  }
  .front-name {
    position: absolute; left: 0; right: 0; top: 282px;
    text-align: center; color: var(--text-light);
    font-weight: 700; font-size: 25px; letter-spacing: 1px; text-transform: uppercase;
  }
  .front-tagline {
    position: absolute; left: 0; right: 0; top: 326px;
    text-align: center; color: var(--text-light);
    font-weight: 500; font-size: 15px; letter-spacing: .8px; text-transform: uppercase;
  }

  /* Back */
  .back-art { position: absolute; inset: 0; }
  .back-badge-name {
    position: absolute; left: 460px; top: 150px; width: 200px;
    text-align: center;
    font-weight: 800; font-size: 22px; line-height: 1.2;
    color: var(--orange); text-transform: uppercase;
  }
  .person { position: absolute; left: 40px; top: 52px; }
  .person-name {
    font-weight: 800; font-size: 36px; color: var(--text-light);
  }
  .person-name .surname { color: var(--orange); }
  .person-role {
    margin-top: 2px; font-weight: 500; font-size: 18px; color: var(--text-soft);
  }
  .address {
    position: absolute; left: 40px; top: 218px;
    font-size: 17px; line-height: 1.35; color: var(--text-light);
  }
  .contacts {
    position: absolute; left: 40px; top: 286px;
    list-style: none; font-size: 17px; line-height: 1.4; color: var(--text-light);
  }
  .contacts li { display: flex; align-items: center; gap: 10px; }
  .contacts svg { width: 14px; height: 14px; flex: none; }
</style>
</head>
<body>
<main class="canvas">

  <section class="card card--front" aria-label="Card front">
    <div class="front-badge"><span class="badge-name">Brackley<br>Earthworks</span></div>
    <h1 class="front-name">Brackley Earthworks</h1>
    <p class="front-tagline">Civil Construction, Quarry &amp; Mining Services</p>
  </section>

  <section class="card card--back" aria-label="Card back">
    <svg class="back-art" viewBox="0 0 700 400" aria-hidden="true">
      <path d="M545 25 A175 175 0 0 0 545 375 L700 375 L700 0 L545 0 Z" fill="var(--card-white)"/>
      <rect x="545" y="0" width="155" height="400" fill="var(--card-white)"/>
      <path d="M395 95 A178 178 0 0 0 545 380" fill="none" stroke="var(--orange)" stroke-width="5"/>
      <circle cx="562" cy="198" r="135" fill="var(--shadow-grey)"/>
      <circle cx="553" cy="192" r="135" fill="var(--card-black)"/>
    </svg>
    <div class="back-badge-name">Brackley<br>Earthworks</div>

    <div class="person">
      <h2 class="person-name">Dana <span class="surname">Whitlock</span></h2>
      <p class="person-role">Payroll Manager</p>
    </div>

    <address class="address" style="font-style:normal">
      42 Quarry Road,<br>Unit 3 Toowoomba QLD 4350
    </address>

    <ul class="contacts">
      <li>
        <svg viewBox="0 0 24 24"><path fill="var(--orange)" d="M6.6 10.8a15 15 0 0 0 6.6 6.6l2.2-2.2c.3-.3.7-.4 1-.2 1.1.4 2.3.6 3.6.6.6 0 1 .4 1 1V20c0 .6-.4 1-1 1A17 17 0 0 1 3 4c0-.6.4-1 1-1h3.5c.6 0 1 .4 1 1 0 1.3.2 2.5.6 3.6.1.3 0 .7-.2 1z"/></svg>
        (07) 4632 5108
      </li>
      <li>
        <svg viewBox="0 0 24 24"><rect x="2" y="5" width="20" height="14" rx="1" fill="none" stroke="var(--orange)" stroke-width="2"/><path d="M2 6l10 7 10-7" fill="none" stroke="var(--orange)" stroke-width="2"/></svg>
        info@brackleyearthworks.com.au
      </li>
      <li>
        <svg viewBox="0 0 24 24"><circle cx="12" cy="12" r="10" fill="var(--orange)"/><path d="M2 12h20M12 2c3 3 3 17 0 20M12 2c-3 3-3 17 0 20" fill="none" stroke="var(--card-black)" stroke-width="1.5"/></svg>
        www.brackleyearthworks.com.au
      </li>
    </ul>
  </section>

</main>
</body>
</html>
```